business card for author of crime novel

I am an author with a new book. I need a business card with the book's cover on one side (already uploaded), and contact details on the other.

Walt Pemberty
Author

telephone: 646-512-7380
website: www.waltpemberty.net
facebook: facebook.com/wpemberty
twitter: twitter.com/wpemberty
email: wpemberty@postvale.net

Target Market(s)

Readers of mystery books

Industry/Entity Type

Business

Contact Information for Business Card

Walt Pemberty
Author

telephone: 646-512-7380

Font styles to use
Serif
Sans Serif

Requirements
Must have
• Book cover on one side. My contact info on the other, with the name of the book repeated if that makes sense. Clean design.
Should not have
• Overly ornate, too formal, too distracting

```html
<!DOCTYPE html>
<html lang="en">
<head>
<meta charset="utf-8">
<title>Walt Pemberty – Business Card</title>
<link rel="stylesheet" href="https://fonts.googleapis.com/css2?family=Montserrat:wght@400;600;700&family=Old+Standard+TT:wght@400;700&display=swap">
<style>
  :root {
    --backdrop: #ecedef;
    --card-white: #fbfbfb;
    --ink: #161616;
    --ink-soft: #6f6f6f;
    --mustard: #cf9428;
    --photo-dark: #1f2a36;
    --photo-mid: #4f6478;
    --photo-light: #9fb0bf;
    --author-yellow: #e6d84a;
    --plaque: #e7c995;
    --plaque-edge: #b98f55;
    --plaque-ink: #2a1d10;
  }
  * { box-sizing: border-box; margin: 0; padding: 0; }
  html, body { width: 1200px; height: 900px; overflow: hidden; }
  body {
    background: var(--backdrop);
    position: relative;
    font-family: "Montserrat", Arial, sans-serif;
  }

  /* Contact side */
  .card-contact {
    position: absolute;
    left: 80px; top: 300px;
    width: 560px; height: 320px;
    background: var(--card-white);
    box-shadow: 0 14px 30px rgba(0,0,0,0.12);
    border-radius: 2px;
  }
  .identity {
    position: absolute;
    right: 290px; top: 92px;
    text-align: right;
  }
  .identity-name {
    font-weight: 700; font-size: 19px; color: var(--ink);
    letter-spacing: 0.2px;
  }
  .identity-role {
    font-size: 13px; color: var(--ink-soft); margin-top: 4px;
  }
  .contact-list {
    position: absolute;
    left: 300px; top: 120px;
    list-style: none;
    font-size: 12.5px;
    line-height: 1.25;
  }
  .contact-label { font-weight: 700; color: var(--ink); }
  .contact-value { color: var(--ink-soft); margin-bottom: 3px; }

  /* Book cover side */
  .card-cover {
    position: absolute;
    left: 720px; top: 150px;
    width: 343px; height: 600px;
    background: var(--mustard);
    box-shadow: 0 14px 30px rgba(0,0,0,0.15);
    border-radius: 2px;
  }
  .cover-title {
    position: absolute;
    left: 0; right: 0; top: 26px;
    text-align: center;
    font-family: "Old Standard TT", Georgia, serif;
    font-weight: 700; font-size: 27px;
    letter-spacing: 1px;
    color: var(--ink);
    word-spacing: 6px;
  }
  .cover-photo {
    position: absolute;
    left: 30px; top: 76px;
    width: 283px; height: 430px;
    background: linear-gradient(160deg, var(--photo-light) 0%, var(--photo-mid) 35%, var(--photo-dark) 100%);
  }
  .cover-author {
    position: absolute;
    right: 44px; top: 380px;
    text-align: center;
    font-family: "Old Standard TT", Georgia, serif;
    font-size: 19px; line-height: 1.2;
    letter-spacing: 1px;
    color: var(--author-yellow);
  }
  .series-plaque {
    position: absolute;
    left: 150px; top: 488px;
    width: 176px; height: 40px;
    background: var(--plaque);
    border: 2px solid var(--plaque-edge);
    border-radius: 5px;
    box-shadow: 0 3px 5px rgba(0,0,0,0.25);
    display: flex; align-items: center; justify-content: center;
    font-family: "Old Standard TT", Georgia, serif;
    font-size: 15px; color: var(--plaque-ink);
  }
</style>
</head>
<body>
  <section class="card-contact">
    <div class="identity">
      <p class="identity-name">Walt Pemberty</p>
      <p class="identity-role">Author</p>
    </div>
    <ul class="contact-list">
      <li><p class="contact-label">telephone</p><p class="contact-value">646-512-7380</p></li>
      <li><p class="contact-label">email</p><p class="contact-value">wpemberty@postvale.net</p></li>
      <li><p class="contact-label">facebook</p><p class="contact-value">facebook.com/wpemberty</p></li>
      <li><p class="contact-label">twitter</p><p class="contact-value">twitter.com/wpemberty</p></li>
    </ul>
  </section>

  <section class="card-cover">
    <h1 class="cover-title">DEAD COLD ALLEY</h1>
    <div class="cover-photo" role="img" aria-label="Cover photograph: old city apartment building with balconies, seen from below in cold blue tones"></div>
    <p class="cover-author">WALT<br>PEMBERTY</p>
    <p class="series-plaque">A Harlan Voss Mystery</p>
  </section>
</body>
</html>
```